BrightWave Tristate Commercial Cleaning Brochure

We need a tri fold brochure that we can use to market our commercial cleaning services to clients. We are looking for something that will stand out. We don't want to use any faces of people on the brochures, only cleaning tools and supplies. We offer Office Cleaning, Covid Cleaning, Janitorial and Floor Services

Target Market(s)

Small to large businesses

Industry/Entity Type

Commercial Cleaning

Colors
0054AA
0677BA
7BADD7
CADEEF
E8F1F8
0094D4
00A9DD
6FCCEA
C7EBF8
E9F6FB
00AB8E
00BBA5
67D7C9
C6EFE9
E9F9F6
59FF00
82FF00
B8FF75
E3FFCB
F4FFEA

Requirements
Must have
• Stand out design-Eye Catching
Should not have
• faces of ppl the brochure

```html
<!DOCTYPE html>
<html lang="en">
<head>
<meta charset="utf-8">
<title>BrightWave Tristate – Commercial Cleaning Brochure</title>
<link rel="stylesheet" href="https://fonts.googleapis.com/css2?family=Quicksand:wght@500;700&family=Open+Sans:wght@400;600&display=swap">
<style>
  :root{
    --blue:#1e6fc3;
    --blue-deep:#0054aa;
    --blue-mid:#2a86d4;
    --blue-pale:#dbecf9;
    --blue-wash:#e9f3fb;
    --sky-top:#cfe3f6;
    --sky-bottom:#e6f1fb;
    --green:#80c341;
    --white:#ffffff;
    --ink:#1b4f93;
    --backdrop:#e6e8f3;
  }
  *{margin:0;padding:0;box-sizing:border-box}
  html,body{width:1047px;height:1200px;overflow:hidden;background:var(--backdrop)}
  .stage{position:absolute;left:0;top:0;width:1200px;height:1376px;transform:scale(.8725);transform-origin:0 0;
    background:linear-gradient(135deg,#f3f3f8,#dfe1ef);font-family:"Open Sans",sans-serif}
  .sheet{position:absolute;width:778px;height:603px;box-shadow:0 4px 14px rgba(40,50,90,.25);overflow:hidden;background:var(--blue-wash)}
  .sheet--outside{left:222px;top:60px}
  .sheet--inside{left:223px;top:710px}
  .sheet__art{position:absolute;inset:0}
  .abs{position:absolute}
  .headline{font-family:"Quicksand",sans-serif;font-weight:700;line-height:1.02;text-align:center}
  .body-copy{font-size:9.1px;line-height:12px;text-align:justify;hyphens:auto;letter-spacing:-.05px}
  .body-copy p+p{margin-top:12px}
  .brand-name{font-family:"Quicksand",sans-serif;font-weight:700;color:var(--blue-deep);text-align:center;line-height:1}
  .url-pill{position:absolute;height:26px;border-radius:14px;background:var(--white);border:3px solid var(--green);
    display:flex;align-items:center;gap:8px;padding-left:5px;font-family:"Quicksand",sans-serif;font-weight:700;font-size:13.5px;color:var(--blue-deep);white-space:nowrap}
  .url-pill--blue{background:var(--blue);border-color:var(--white);color:var(--white)}
  .globe{width:18px;height:18px;flex:none}
  .rule{position:absolute;height:5px;width:56px;border-radius:3px}
  .contact-list{list-style:none;font-family:"Quicksand",sans-serif;font-weight:700;font-size:12px;color:var(--blue-deep)}
  .contact-list li{display:flex;gap:6px;align-items:flex-start;margin-bottom:3px}
  .contact-list svg{width:13px;height:13px;flex:none;margin-top:1px}
  .contact-pill{background:var(--blue);color:var(--white);font-family:"Quicksand",sans-serif;font-weight:700;font-size:14px;
    border-radius:9px;width:128px;text-align:center;line-height:17px}
</style>
</head>
<body>
<div class="stage">

  <!-- Outside spread -->
  <section class="sheet sheet--outside">
    <svg class="sheet__art" viewBox="0 0 778 603" width="778" height="603">
      <defs>
        <linearGradient id="sky" x1="0" y1="0" x2="0" y2="1"><stop offset="0" stop-color="#cfe3f6"/><stop offset="1" stop-color="#e6f1fb"/></linearGradient>
        <linearGradient id="skyTop" gradientUnits="userSpaceOnUse" x1="0" y1="0" x2="0" y2="603"><stop offset="0" stop-color="#cfe3f6"/><stop offset="1" stop-color="#e6f1fb"/></linearGradient>
        <linearGradient id="floorPhoto" x1="0" y1="0" x2="1" y2="1"><stop offset="0" stop-color="#eef0f2"/><stop offset="1" stop-color="#a9adb4"/></linearGradient>
        <linearGradient id="cartPhoto" x1="0" y1="0" x2="0" y2="1"><stop offset="0" stop-color="#f0f0f0"/><stop offset=".6" stop-color="#dadada"/><stop offset="1" stop-color="#c8c8c8"/></linearGradient>
      </defs>
      <rect x="258" y="0" width="257" height="603" fill="url(#skyTop)"/>
      <g role="img" aria-label="Photo of a floor scrubber machine on a bright office floor">
        <rect x="0" y="22" width="258" height="170" fill="url(#floorPhoto)"/>
      </g>
      <rect x="515" y="22" width="263" height="126" fill="var(--white)"/>
      <g role="img" aria-label="Photo of a cleaning cart with buckets, sprays, gloves and cloths">
        <rect x="515" y="148" width="263" height="320" fill="url(#cartPhoto)"/>
      </g>
      <!-- map circle, top tucked under the wave -->
      <circle cx="362" cy="210" r="104" fill="var(--white)" stroke="#d7e3ee" stroke-width="2"/>
      <path d="M411,118 A104,104 0 0 1 330,309" fill="none" stroke="var(--green)" stroke-width="3"/>
      <path d="M258,0 H515 V150 C440,134 360,124 258,128 Z" fill="url(#skyTop)"/>
      <path d="M0,170 C90,140 190,115 290,120 C390,125 460,138 515,150 L515,168 C440,150 360,140 280,140 C180,140 90,165 0,195 Z" fill="var(--green)"/>
      <path d="M0,190 C90,162 180,145 258,142 L258,603 L0,603 Z" fill="var(--blue)"/>
      <path d="M418,603 C440,480 600,395 778,425 L778,603 Z" fill="var(--green)"/>
      <path d="M432,603 C455,492 610,410 778,438 L778,603 Z" fill="var(--blue)"/>
      <rect x="0" y="0" width="778" height="22" fill="var(--blue-mid)"/>
    </svg>

    <h2 class="headline abs" style="left:40px;top:210px;width:220px;font-size:34px;color:var(--white)">Floor<br>Cleaning</h2>
    <div class="body-copy abs" style="left:23px;top:298px;width:215px;color:var(--white)">
      <p>Lorem ipsum dolor sit amet, consectetur adipiscing elit. Sed volutpat pretium pharetra. Maecenas porta diam justo, vitae hendrerit nisi commodo et. Quisque eu metus condimentum, suscipit augue nec, hendrerit enim. Fusce vitae fringilla nisi, ultrices congue urna. In porttitor lacinia mi at accumsan. Donec pharetra mi a sem cursus congue. Curabitur suscipit consectetur dolor, sed rhoncus diam porta vel. Sed consequat egestas bibendum. Proin nec ex est.</p>
      <p>Phasellus rutrum, libero eu consequat semper, felis libero vestibulum odio, sit amet dignissim nulla tortor at urna. Nunc dignissim ullamcorper urna, non vulputate dolor interdum sed. Sed laoreet tempor lectus, dapibus ornare tellus commodo ac. Praesent faucibus tincidunt faucibus. Suspendisse tristique, nisl sit amet sollicitudin laoreet, orci felis scelerisque lectus, ut lobortis tellus est sed eros. In hac habitasse platea dictumst. Praesent enim quam, tincidunt pellentesque mauris in, imperdiet lobortis magna. Praesent non blandit leo. Morbi et quam felis.</p>
    </div>

    <svg class="abs" style="left:308px;top:32px" width="150" height="26" viewBox="0 0 150 26" aria-label="Five stars">
      <g fill="var(--blue)">
        <polygon points="13,1 16,9 25,9 18,14 21,23 13,17 5,23 8,14 1,9 10,9"/>
        <polygon transform="translate(31 0)" points="13,1 16,9 25,9 18,14 21,23 13,17 5,23 8,14 1,9 10,9"/>
        <polygon transform="translate(62 0)" points="13,1 16,9 25,9 18,14 21,23 13,17 5,23 8,14 1,9 10,9"/>
        <polygon transform="translate(93 0)" points="13,1 16,9 25,9 18,14 21,23 13,17 5,23 8,14 1,9 10,9"/>
        <polygon transform="translate(124 0)" points="13,1 16,9 25,9 18,14 21,23 13,17 5,23 8,14 1,9 10,9"/>
      </g>
    </svg>
    <p class="headline abs" style="left:262px;top:64px;width:250px;font-size:16.5px;color:var(--ink);line-height:1.3">Your <span style="color:var(--blue-mid)">TOP RATED</span> DMV<br>Commercial Cleaning Team</p>
    <p class="abs" style="left:305px;top:200px;width:115px;text-align:center;font-family:Quicksand,sans-serif;font-weight:700;font-size:24px;color:#c9ccd0">MAP</p>

    <p class="brand-name abs" style="left:270px;top:372px;width:235px;font-size:28px">BrightWave<br><span style="font-size:19px">Tristate</span></p>
    <p class="contact-pill abs" style="left:289px;top:434px">CONTACT US</p>
    <ul class="contact-list abs" style="left:290px;top:464px;width:200px">
      <li><svg viewBox="0 0 14 14"><circle cx="7" cy="7" r="7" fill="var(--green)"/><rect x="3.5" y="4.5" width="7" height="5" fill="none" stroke="#fff"/><path d="M3.5,4.5 7,7.5 10.5,4.5" fill="none" stroke="#fff"/></svg>Email</li>
      <li><svg viewBox="0 0 14 14"><circle cx="7" cy="7" r="7" fill="var(--green)"/><path d="M7,11 C4,7.5 4,5 7,3.5 C10,5 10,7.5 7,11Z" fill="#fff"/><circle cx="7" cy="6" r="1.2" fill="var(--green)"/></svg>Address<br>Address</li>
      <li><svg viewBox="0 0 14 14"><circle cx="7" cy="7" r="7" fill="var(--green)"/><path d="M4.5,3.5 6,5.5 5.2,6.5 7.5,8.8 8.5,8 10.5,9.5 9.5,10.8 C6.5,10.5 3.5,7.5 3.2,4.5Z" fill="#fff"/></svg>Phone Number</li>
      <li><svg viewBox="0 0 14 14"><circle cx="7" cy="7" r="7" fill="var(--green)"/><rect x="4" y="5.5" width="6" height="4" fill="#fff"/><rect x="5" y="3.5" width="4" height="2" fill="#fff"/></svg>Fax Number</li>
    </ul>

    <p class="brand-name abs" style="left:530px;top:46px;width:235px;font-size:36px">BrightWave<br><span style="font-size:22px">Tristate</span></p>
    <p class="headline abs" style="left:530px;top:472px;width:235px;font-size:22px;color:var(--white)">YOUR TOP RATED</p>
    <p class="headline abs" style="left:530px;top:503px;width:235px;font-size:16px;color:var(--white)">DMV Commercial<br>Cleaning Team</p>
    <div class="url-pill" style="left:526px;top:558px;width:232px">
      <svg class="globe" viewBox="0 0 18 18"><circle cx="9" cy="9" r="9" fill="var(--blue)"/><g fill="none" stroke="#fff" stroke-width="1"><circle cx="9" cy="9" r="5.5"/><ellipse cx="9" cy="9" rx="2.3" ry="5.5"/><path d="M3.5,9h11"/></g></svg>
      www.brightwavetristate.com
    </div>
  </section>

  <!-- Inside spread -->
  <section class="sheet sheet--inside">
    <svg class="sheet__art" viewBox="0 0 779 603" width="779" height="603">
      <defs>
        <linearGradient id="virusPhoto" x1="0" y1="0" x2="1" y2="1"><stop offset="0" stop-color="#6e8ea8"/><stop offset="1" stop-color="#2c3d4d"/></linearGradient>
        <linearGradient id="janitorPhoto" x1="0" y1="0" x2="0" y2="1"><stop offset="0" stop-color="#e9ecef"/><stop offset="1" stop-color="#b7c1cf"/></linearGradient>
        <linearGradient id="officePhoto" x1="0" y1="0" x2="1" y2="0"><stop offset="0" stop-color="#dfe4ea"/><stop offset="1" stop-color="#9ea6ae"/></linearGradient>
      </defs>
      <rect x="0" y="0" width="779" height="603" fill="var(--white)"/>
      <rect x="0" y="110" width="264" height="473" fill="var(--blue-pale)"/>
      <rect x="264" y="100" width="257" height="483" fill="var(--blue)"/>
      <g role="img" aria-label="Photo of gloved hands spraying and wiping a surface with virus particles in the air">
        <rect x="521" y="20" width="258" height="140" fill="url(#virusPhoto)"/>
      </g>
      <path d="M521,118 C600,140 700,138 779,118 L779,603 L521,603 Z" fill="var(--blue)"/>
      <path d="M521,132 C600,154 700,152 779,132 L779,603 L521,603 Z" fill="var(--green)"/>
      <!-- white sweep under the green wave -->
      <path d="M0,0 H521 V112 C330,98 160,124 0,162 Z" fill="var(--white)"/>
      <path d="M0,118 C140,100 330,72 521,84 L521,104 C330,94 160,118 0,150 Z" fill="var(--green)"/>
      <path d="M521,84 C600,90 680,112 779,108 L779,118 C700,138 600,140 521,118 Z" fill="var(--green)"/>
      <g role="img" aria-label="Photo of a worker carrying a bucket of supplies and a broom">
        <rect x="0" y="415" width="263" height="168" fill="url(#janitorPhoto)"/>
      </g>
      <g role="img" aria-label="Photo of a gloved hand wiping an office desk beside a keyboard">
        <rect x="264" y="413" width="257" height="170" fill="url(#officePhoto)"/>
      </g>
      <rect x="0" y="0" width="779" height="20" fill="var(--blue-mid)"/>
      <rect x="0" y="583" width="779" height="20" fill="var(--blue-mid)"/>
    </svg>

    <h3 class="abs" style="left:17px;top:26px;font-family:Quicksand,sans-serif;font-weight:700;font-size:17px;color:var(--blue-mid)">About <span style="color:var(--ink)">Us</span></h3>
    <p class="abs" style="left:17px;top:46px;width:492px;font-size:9.3px;line-height:12px;color:#222">Lorem ipsum dolor sit amet, consectetur adipiscing elit. Sed volutpat pretium pharetra. Maecenas porta diam justo, vitae hendrerit nisi commodo et. Quisque eu metus condimentum, suscipit augue nec, hendrerit enim. Fusce vitae fringilla nisi, ultrices congue urna.</p>

    <h2 class="headline abs" style="left:0;top:176px;width:264px;font-size:30px;color:var(--blue-mid)">Janitorial</h2>
    <span class="rule" style="left:104px;top:213px;background:var(--green)"></span>
    <div class="body-copy abs" style="left:25px;top:247px;width:215px;color:var(--ink)">
      <p>Lorem ipsum dolor sit amet, consectetur adipiscing elit. Sed volutpat pretium pharetra. Maecenas porta diam justo, vitae hendrerit nisi commodo et. Quisque eu metus condimentum, suscipit augue nec, hendrerit enim. Fusce vitae fringilla nisi, ultrices congue urna. In porttitor lacinia mi at accumsan. Donec pharetra mi a sem cursus congue. Curabitur suscipit consectetur dolor, sed rhoncus diam porta vel. Sed consequat egestas bibendum. Proin nec ex est.</p>
    </div>

    <h2 class="headline abs" style="left:264px;top:140px;width:257px;font-size:30px;color:var(--white)">Office<br>Cleaning</h2>
    <span class="rule" style="left:364px;top:207px;background:var(--green)"></span>
    <div class="body-copy abs" style="left:284px;top:244px;width:215px;color:var(--white)">
      <p>Lorem ipsum dolor sit amet, consectetur adipiscing elit. Sed volutpat pretium pharetra. Maecenas porta diam justo, vitae hendrerit nisi commodo et. Quisque eu metus condimentum, suscipit augue nec, hendrerit enim. Fusce vitae fringilla nisi, ultrices congue urna. In porttitor lacinia mi at accumsan. Donec pharetra mi a sem cursus congue. Curabitur suscipit consectetur dolor, sed rhoncus diam porta vel. Sed consequat egestas bibendum. Proin nec ex est.</p>
    </div>

    <h2 class="headline abs" style="left:521px;top:175px;width:258px;font-size:29px;color:var(--white)">Covid Cleaning</h2>
    <span class="rule" style="left:554px;top:211px;background:var(--blue)"></span>
    <div class="body-copy abs" style="left:543px;top:245px;width:215px;color:var(--white)">
      <p>Lorem ipsum dolor sit amet, consectetur adipiscing elit. Sed volutpat pretium pharetra. Maecenas porta diam justo, vitae hendrerit nisi commodo et. Quisque eu metus condimentum, suscipit augue nec, hendrerit enim. Fusce vitae fringilla nisi, ultrices congue urna. In porttitor lacinia mi at accumsan. Donec pharetra mi a sem cursus congue. Curabitur suscipit consectetur dolor, sed rhoncus diam porta vel. Sed consequat egestas bibendum. Proin nec ex est.</p>
      <p>Phasellus rutrum, libero eu consequat semper, felis libero vestibulum odio, sit amet dignissim nulla tortor at urna. Nunc dignissim ullamcorper urna, non vulputate dolor interdum sed. Sed laoreet tempor lectus, dapibus ornare tellus commodo ac. Praesent faucibus tincidunt faucibus. Suspendisse tristique, nisl sit amet sollicitudin laoreet, orci felis scelerisque lectus, ut lobortis tellus est sed eros. In hac habitasse platea dictumst. Praesent enim quam, tincidunt pellentesque mauris in, imperdiet lobortis magna. Praesent non blandit leo.</p>
    </div>
    <div class="url-pill url-pill--blue" style="left:531px;top:544px;width:232px">
      <svg class="globe" viewBox="0 0 18 18"><circle cx="9" cy="9" r="9" fill="var(--white)"/><g fill="none" stroke="var(--blue)" stroke-width="1"><circle cx="9" cy="9" r="5.5"/><ellipse cx="9" cy="9" rx="2.3" ry="5.5"/><path d="M3.5,9h11"/></g></svg>
      www.brightwavetristate.com
    </div>
  </section>

</div>
</body>
</html>
```